Lantern Vigor
Basketball Fitness Training
Lantern Vigor -
Creative Brief
Modern
Doran Fisk
Health and Fitness Coach
tavmirlo@quillpost.example
www.lanternvigor.example
Youth Development Clinics Private 1 on 1 Sessions Executive Training Women's Fitness Cross Training

```html
<!DOCTYPE html>
<html lang="en">
<head>
<meta charset="UTF-8">
<title>Lantern Vigor – Business Card</title>
<link rel="stylesheet" href="https://fonts.googleapis.com/css2?family=Russo+One&family=Noto+Serif:wght@700&family=Open+Sans:wght@400;600&display=swap">
<style>
  :root {
    --page-bg: #e9e6e1;
    --card-bg: #ffffff;
    --ink: #111111;
    --navy: #1f3f95;
    --orange: #ef5a1d;
    --grey-text: #555a60;
    --divider: #c9ccd1;
  }
  * { margin: 0; padding: 0; box-sizing: border-box; }
  html, body {
    width: 1200px;
    height: 780px;
    overflow: hidden;
    background: var(--page-bg);
  }
  .canvas {
    position: relative;
    width: 1200px;
    height: 780px;
    display: flex;
    align-items: center;
    justify-content: center;
  }
  .card {
    position: relative;
    width: 1120px;
    height: 700px;
    background: var(--card-bg);
    border-radius: 44px;
    overflow: hidden;
    box-shadow: 0 4px 18px rgba(0,0,0,0.12);
  }
  .brand {
    position: absolute;
    top: 90px;
    left: 150px;
    display: flex;
    align-items: center;
    gap: 34px;
  }
  .brand-dot {
    width: 120px;
    height: 120px;
    border-radius: 50%;
    background: var(--orange);
    flex: none;
  }
  .brand-name {
    font-family: "Russo One", sans-serif;
    font-size: 96px;
    line-height: 1;
    color: var(--ink);
    letter-spacing: 1px;
  }
  .brand-tagline {
    margin-top: 10px;
    font-family: "Russo One", sans-serif;
    font-size: 34px;
    color: var(--ink);
    letter-spacing: 0.5px;
  }
  .contact-block {
    position: absolute;
    top: 400px;
    left: 0;
    width: 100%;
    display: flex;
    align-items: center;
  }
  .person {
    width: 520px;
    text-align: right;
    padding-right: 30px;
  }
  .person-name {
    font-family: "Noto Serif", serif;
    font-weight: 700;
    font-size: 44px;
    color: var(--navy);
  }
  .person-role {
    margin-top: 8px;
    font-family: "Open Sans", sans-serif;
    font-size: 28px;
    color: var(--orange);
  }
  .divider {
    width: 2px;
    height: 130px;
    background: var(--divider);
  }
  .details {
    list-style: none;
    padding-left: 24px;
    font-family: "Open Sans", sans-serif;
    font-size: 24px;
    color: var(--grey-text);
  }
  .details li {
    display: flex;
    align-items: center;
    gap: 14px;
    line-height: 1;
  }
  .details li + li { margin-top: 26px; }
  .details svg { width: 26px; height: 26px; flex: none; }
  .swoosh {
    position: absolute;
    left: 0;
    bottom: 0;
    width: 1120px;
    height: 200px;
  }
</style>
</head>
<body>
<main class="canvas">
  <article class="card">
    <header class="brand">
      <span class="brand-dot" aria-hidden="true"></span>
      <div>
        <h1 class="brand-name">Lantern Vigor</h1>
        <p class="brand-tagline">Basketball Fitness Training</p>
      </div>
    </header>

    <section class="contact-block">
      <div class="person">
        <h2 class="person-name">Doran Fisk</h2>
        <p class="person-role">Health and Fitness Coach</p>
      </div>
      <span class="divider" aria-hidden="true"></span>
      <ul class="details">
        <li>
          <svg viewBox="0 0 24 24" aria-hidden="true"><circle cx="12" cy="12" r="4" fill="none" stroke="#1f3f95" stroke-width="2.4"/><path d="M16 8v5a2.5 2.5 0 0 0 5 0v-1a9 9 0 1 0-3.5 7.1" fill="none" stroke="#1f3f95" stroke-width="2.4" stroke-linecap="round"/></svg>
          <span>tavmirlo@quillpost.example</span>
        </li>
        <li>
          <svg viewBox="0 0 24 24" aria-hidden="true"><circle cx="12" cy="12" r="10" fill="#1f3f95"/><path d="M2 12h20M12 2c3 3 3 17 0 20M12 2c-3 3-3 17 0 20M4.5 6.5h15M4.5 17.5h15" fill="none" stroke="#fff" stroke-width="1.2"/></svg>
          <span>www.lanternvigor.example</span>
        </li>
      </ul>
    </section>

    <svg class="swoosh" viewBox="0 0 1120 200" preserveAspectRatio="none" aria-hidden="true">
      <path d="M0 40 C 250 10, 420 130, 700 80 S 1000 10, 1120 30 L1120 56 C 1000 40, 900 90, 700 110 S 250 50, 0 70 Z" fill="var(--orange)"/>
      <path d="M0 95 C 250 70, 450 170, 720 125 S 1000 55, 1120 70 L1120 200 L0 200 Z" fill="var(--navy)"/>
    </svg>
  </article>
</main>
</body>
</html>
```